Web design for Frostwerkly.com

We need a website (4 starter pages) designed for a drupal based site. The theme is flexible so I am open to different designs/looks. I am looking for a VERY simple and clean and FUN design to make it easy to use for the customer.

Our company is similar to Pitch lantern as in it's for multiple people to design a cake for a customer and they choose a winning design and work with that cake designer to make the cake (birthday, wedding etc...)

Our vision:
First page:
2 main images for either the customer to submit an idea for a cake, or the new designer to sign up to the site. Perhaps a mouse-over with wording on what the options are? You can use this site:
http://www.plumwidget.example/ as a sort of template but more clean and simple

"How it works" page:
Similar to this:
http://www.plumwidget.example/how-it-works
Fun, clean and simple

Submit cake design page (form submission)

Submit new designer page

Ideally a 960 wide design with no flash, but open to a flash design if it stands out...

Please contact me if you have any questions!

Target Market(s)

People who want a custom cake made, and people who design and make cakes.

Industry/Entity Type

Wedding

Requirements
Must have
• Use the logo attached. The "Tater Bop" should be a big part of the site...kind of a site mascot?
Nice to have
• 960 wide
No flash but not a deal-breaker if there is flash and it's amazing...

```html
<!DOCTYPE html>
<html lang="en">
<head>
<meta charset="utf-8">
<title>Frostwerkly.com – Wedding cake Mara and Theo</title>
<link rel="stylesheet" href="https://fonts.googleapis.com/css2?family=Dosis:wght@500;600;700;800&family=Varela+Round&display=swap">
<style>
:root{
  --bg-brown:#4f342a;
  --footer-brown:#4a3026;
  --paper:#f3efe8;
  --paper-stripe:#efe9e1;
  --frame:#a3918a;
  --ink:#4d3a33;
  --ink-soft:#7a6a63;
  --teal:#5fb3b3;
  --teal-dark:#3f9a9c;
  --teal-shade:#2f7f82;
  --pink:#e79ab5;
  --pink-soft:#f6d6e1;
  --heart-line:#c9a9b4;
  --btn:#ddd4cb;
  --btn-line:#a99b92;
  --card:#faf8f4;
  --card-line:#e4dbd2;
  --footer-text:#b7a49b;
}
*{box-sizing:border-box;margin:0;padding:0}
html,body{width:1200px;height:1200px;overflow:hidden}
body{background:var(--bg-brown);font-family:"Varela Round",sans-serif;color:var(--ink);position:relative}
.abs{position:absolute}
.page-shape{position:absolute;left:0;top:0}
.footer{position:absolute;left:112px;top:984px;width:976px;height:216px;background:var(--footer-brown)}
.gingham{position:absolute;left:112px;top:938px;width:976px;height:48px;
  background:linear-gradient(180deg,#f2c9d6,#e59bb4 50%,#f2c9d6)}
.logo{position:absolute;left:157px;top:88px;display:flex;align-items:center;gap:10px}
.logo-mark{width:52px;height:52px;border-radius:50%;background:var(--pink-soft)}
.logo-name{font-family:"Dosis",sans-serif;font-weight:700;font-size:42px;color:var(--ink);letter-spacing:-.5px}
.nav{position:absolute;left:667px;top:126px;height:30px;display:flex;align-items:center}
.nav a{font-family:"Dosis",sans-serif;font-weight:700;font-size:12.5px;letter-spacing:2px;color:#fff;text-decoration:none;text-align:center;line-height:30px;border-left:1px dashed rgba(255,255,255,.6)}
.nav a:first-child{border-left:none}
.nav .you{background:var(--teal-dark)}
.help{display:inline-block;width:22px;height:15px;background:#fff;border-radius:3px;color:var(--teal-dark);font-size:11px;line-height:15px;vertical-align:middle}
.subnav{position:absolute;top:165px;display:flex;gap:8px;left:846px}
.btn{display:inline-block;height:20px;line-height:18px;padding:0 10px;background:var(--btn);border:1px solid var(--btn-line);border-radius:3px;font-family:"Dosis",sans-serif;font-weight:700;font-size:12px;color:var(--ink);text-align:center;box-shadow:inset 0 1px 0 #f7f3ee}
.contest-title{position:absolute;left:157px;top:211px;font-family:"Dosis",sans-serif;font-weight:800;font-size:20px;letter-spacing:2.6px;color:#fff;-webkit-text-stroke:1.2px var(--ink);text-transform:uppercase}
.contest-meta{position:absolute;right:155px;top:213px;font-family:"Dosis",sans-serif;font-weight:600;font-size:16px;color:var(--ink)}
.contest-meta b{color:var(--teal);font-weight:700}
.filters{position:absolute;left:157px;top:272px;display:flex;gap:7px}
.filters .btn{padding:0 7px;letter-spacing:.6px}
.grid{position:absolute;left:157px;top:315px;width:886px}
.row{position:relative;height:202.5px}
.entry{position:absolute;top:0;width:136px}
.thumb{width:136px;height:101px;background:var(--card);border:1px solid var(--card-line);box-shadow:0 1px 3px rgba(80,50,40,.15);padding:7px}
.photo{width:100%;height:100%;border:1px solid #d8d0c8}
.rating{display:flex;gap:4.7px;margin-top:13px}
.rating svg{width:15px;height:14px}
.divider{position:absolute;left:0;top:157.5px;width:886px;border-top:2px dotted #b8aba3}
.pager{position:absolute;right:160px;top:898px;font-size:12.5px;color:var(--ink)}
.footer-col{position:absolute;top:1004px;font-size:12.5px;line-height:18.75px;color:var(--footer-text);list-style:none}
.social{position:absolute;top:1000px;left:991px;display:flex;gap:6px}
.social span{width:23px;height:23px;border-radius:50%;background:var(--teal)}
.copyright{position:absolute;right:158px;top:1041px;text-align:right;font-size:12.5px;line-height:18.75px;color:var(--footer-text)}
</style>
</head>
<body>

<svg class="page-shape" width="1200" height="1200" viewBox="0 0 1200 1200" aria-hidden="true">
  <defs>
    <filter id="ribbonShadow" x="-5%" y="-30%" width="110%" height="160%">
      <feDropShadow dx="0" dy="2" stdDeviation="2" flood-color="#5a3c30" flood-opacity=".25"/>
    </filter>
    <pattern id="paperStripes" width="80" height="10" patternUnits="userSpaceOnUse">
      <rect width="80" height="10" fill="var(--paper)"/>
      <rect width="40" height="10" fill="var(--paper-stripe)"/>
    </pattern>
  </defs>
  <!-- sheet -->
  <path d="M112 986 V92 Q112 84 120 84 Q140 84 145 62 Q147 49 160 49 H1040 Q1053 49 1055 62 Q1060 84 1080 84 Q1088 84 1088 92 V986 Z" fill="#e9e1d8" stroke="var(--frame)" stroke-width="3"/>
  <path d="M121 986 V100 Q121 94 127 94 Q148 94 154 70 Q156 59 166 59 H1034 Q1044 59 1046 70 Q1052 94 1073 94 Q1079 94 1079 100 V986 Z" fill="url(#paperStripes)" stroke="var(--frame)" stroke-width="2"/>
  <path d="M131 986 V100 M1069 986 V100" stroke="#c7b9b1" stroke-width="1"/>
  <!-- heading ribbon tails -->
  <polygon points="75,212 112,212 112,258 75,258 92,235" fill="#ded6cd"/>
  <polygon points="1125,212 1088,212 1088,258 1125,258 1108,235" fill="#ded6cd"/>
  <polygon points="98,244 112,244 112,258" fill="#b9aaa1"/>
  <polygon points="1102,244 1088,244 1088,258" fill="#b9aaa1"/>
  <rect x="98" y="198" width="1004" height="46" fill="#f2ede6" filter="url(#ribbonShadow)"/>
  <!-- nav ribbon -->
  <polygon points="1102,140 1125,144 1112,156 1125,170 1102,170" fill="var(--teal)"/>
  <polygon points="1092,156 1102,156 1102,170" fill="var(--teal-shade)"/>
  <polygon points="667,126 1102,126 1102,156 667,156 679,141" fill="var(--teal)"/>
</svg>

<div class="gingham" role="img" aria-label="Pink gingham border band"></div>
<div class="footer"></div>

<div class="logo">
  <span class="logo-mark"></span>
  <span class="logo-name">Frostwerkly.com</span>
</div>

<nav class="nav">
  <a href="#" style="width:83px;padding-left:8px">HOME</a>
  <a href="#" style="width:80px">BROWSE</a>
  <a href="#" style="width:80px">TOUR</a>
  <a href="#" style="width:80px">CONTACT</a>
  <a href="#" class="you" style="width:75px">YOU</a>
  <a href="#" style="width:37px"><span class="help">?</span></a>
</nav>
<div class="subnav">
  <span class="btn" style="width:94px">Contest(s)</span>
  <span class="btn" style="width:102px">Profile</span>
</div>

<h1 class="contest-title">Wedding cake Mara and Theo</h1>
<div class="contest-meta"><b>48</b> entries - End 24 february 2012</div>

<div class="filters">
  <span class="btn">Sort by rating</span>
  <span class="btn">Unrated entries</span>
  <span class="btn">Send poll galery</span>
</div>

<svg width="0" height="0" style="position:absolute" aria-hidden="true">
  <defs>
    <symbol id="heart" viewBox="0 0 16 15">
      <path d="M8 14 C3 10 1 7.5 1 4.8 C1 2.6 2.7 1 4.6 1 C6 1 7.2 1.8 8 3 C8.8 1.8 10 1 11.4 1 C13.3 1 15 2.6 15 4.8 C15 7.5 13 10 8 14 Z"/>
    </symbol>
    <linearGradient id="halfFill" x1="0" x2="0" y1="0" y2="1">
      <stop offset=".5" stop-color="#fff"/><stop offset=".5" stop-color="#e79ab5"/>
    </linearGradient>
  </defs>
</svg>

<div class="grid">
  <div class="row">
    <div class="entry" style="left:0"><div class="thumb"><div class="photo" role="img" aria-label="Tiered blue and white cake on a life ring" style="background:linear-gradient(180deg,#fff 0%,#8fb4e6 40%,#f4f0ea 60%,#f08a4c 85%,#fff)"></div></div>
      <div class="rating"><svg fill="var(--pink)" stroke="var(--heart-line)"><use href="#heart"/></svg><svg fill="var(--pink)" stroke="var(--heart-line)"><use href="#heart"/></svg><svg fill="var(--pink)" stroke="var(--heart-line)"><use href="#heart"/></svg><svg fill="url(#halfFill)" stroke="var(--heart-line)"><use href="#heart"/></svg><svg fill="#fff" stroke="var(--heart-line)"><use href="#heart"/></svg></div></div>
    <div class="entry" style="left:150px"><div class="thumb"><div class="photo" role="img" aria-label="Cupcakes with heart toppers" style="background:linear-gradient(180deg,#f0a9c0,#c03a5a 45%,#e8d8c8 65%,#7a3a2e)"></div></div>
      <div class="rating"><svg fill="var(--pink)" stroke="var(--heart-line)"><use href="#heart"/></svg><svg fill="var(--pink)" stroke="var(--heart-line)"><use href="#heart"/></svg><svg fill="var(--pink)" stroke="var(--heart-line)"><use href="#heart"/></svg><svg fill="#fff" stroke="var(--heart-line)"><use href="#heart"/></svg><svg fill="#fff" stroke="var(--heart-line)"><use href="#heart"/></svg></div></div>
    <div class="entry" style="left:300px"><div class="thumb"><div class="photo" role="img" aria-label="Chocolate cake with cherries" style="background:radial-gradient(ellipse at 50% 45%,#8a5536 0%,#6b3e26 45%,#eee9e4 70%,#fff)"></div></div>
      <div class="rating"><svg fill="var(--pink)" stroke="var(--heart-line)"><use href="#heart"/></svg><svg fill="var(--pink)" stroke="var(--heart-line)"><use href="#heart"/></svg><svg fill="#fff" stroke="var(--heart-line)"><use href="#heart"/></svg><svg fill="#fff" stroke="var(--heart-line)"><use href="#heart"/></svg><svg fill="#fff" stroke="var(--heart-line)"><use href="#heart"/></svg></div></div>
    <div class="entry" style="left:450px"><div class="thumb"><div class="photo" role="img" aria-label="Dark chocolate cake with a slice cut" style="background:radial-gradient(ellipse at 55% 40%,#3a2218 0%,#4b2e20 35%,#f2f2f2 65%,#fff)"></div></div>
      <div class="rating"><svg fill="var(--pink)" stroke="var(--heart-line)"><use href="#heart"/></svg><svg fill="var(--pink)" stroke="var(--heart-line)"><use href="#heart"/></svg><svg fill="#fff" stroke="var(--heart-line)"><use href="#heart"/></svg><svg fill="#fff" stroke="var(--heart-line)"><use href="#heart"/></svg><svg fill="#fff" stroke="var(--heart-line)"><use href="#heart"/></svg></div></div>
    <div class="entry" style="left:600px"><div class="thumb"><div class="photo" role="img" aria-label="Pink frosted cupcake close-up" style="background:linear-gradient(135deg,#e68fb0,#f6d2de 50%,#e27fa4)"></div></div>
      <div class="rating"><svg fill="var(--pink)" stroke="var(--heart-line)"><use href="#heart"/></svg><svg fill="var(--pink)" stroke="var(--heart-line)"><use href="#heart"/></svg><svg fill="var(--pink)" stroke="var(--heart-line)"><use href="#heart"/></svg><svg fill="var(--pink)" stroke="var(--heart-line)"><use href="#heart"/></svg><svg fill="url(#halfFill)" stroke="var(--heart-line)"><use href="#heart"/></svg></div></div>
    <div class="entry" style="left:750px"><div class="thumb"><div class="photo" role="img" aria-label="Stand of cupcakes with pink roses" style="background:radial-gradient(ellipse at 50% 55%,#f0b8c8 0%,#e9c9a8 40%,#f6f0ea 75%)"></div></div>
      <div class="rating"><svg fill="var(--pink)" stroke="var(--heart-line)"><use href="#heart"/></svg><svg fill="var(--pink)" stroke="var(--heart-line)"><use href="#heart"/></svg><svg fill="var(--pink)" stroke="var(--heart-line)"><use href="#heart"/></svg><svg fill="url(#halfFill)" stroke="var(--heart-line)"><use href="#heart"/></svg><svg fill="#fff" stroke="var(--heart-line)"><use href="#heart"/></svg></div></div>
    <div class="divider"></div>
  </div>

  <div class="row">
    <div class="entry" style="left:0"><div class="thumb"><div class="photo" role="img" aria-label="Number five chocolate birthday cake" style="background:radial-gradient(ellipse at 50% 55%,#7a4520 0%,#9a5a2a 25%,#fff 55%)"></div></div>
      <div class="rating"><svg fill="var(--pink)" stroke="var(--heart-line)"><use href="#heart"/></svg><svg fill="#fff" stroke="var(--heart-line)"><use href="#heart"/></svg><svg fill="#fff" stroke="var(--heart-line)"><use href="#heart"/></svg><svg fill="#fff" stroke="var(--heart-line)"><use href="#heart"/></svg><svg fill="#fff" stroke="var(--heart-line)"><use href="#heart"/></svg></div></div>
    <div class="entry" style="left:150px"><div class="thumb"><div class="photo" role="img" aria-label="Tiered chocolate cake with chocolate roses" style="background:radial-gradient(ellipse at 50% 50%,#4a2718 0%,#6a3a24 22%,#fff 50%)"></div></div>
      <div class="rating"><svg fill="var(--pink)" stroke="var(--heart-line)"><use href="#heart"/></svg><svg fill="var(--pink)" stroke="var(--heart-line)"><use href="#heart"/></svg><svg fill="#fff" stroke="var(--heart-line)"><use href="#heart"/></svg><svg fill="#fff" stroke="var(--heart-line)"><use href="#heart"/></svg><svg fill="#fff" stroke="var(--heart-line)"><use href="#heart"/></svg></div></div>
    <div class="entry" style="left:300px"><div class="thumb"><div class="photo" role="img" aria-label="White tiered wedding cake with pink flowers and champagne glasses" style="background:radial-gradient(ellipse at 45% 55%,#f3dbe3 0%,#f7eef1 35%,#fff 60%)"></div></div>
      <div class="rating"><svg fill="var(--pink)" stroke="var(--heart-line)"><use href="#heart"/></svg><svg fill="var(--pink)" stroke="var(--heart-line)"><use href="#heart"/></svg><svg fill="var(--pink)" stroke="var(--heart-line)"><use href="#heart"/></svg><svg fill="url(#halfFill)" stroke="var(--heart-line)"><use href="#heart"/></svg><svg fill="#fff" stroke="var(--heart-line)"><use href="#heart"/></svg></div></div>
    <div class="entry" style="left:450px"><div class="thumb"><div class="photo" role="img" aria-label="Pink ribboned gift-style cake on grey" style="background:linear-gradient(180deg,#a9a9ab,#d9d4d8 40%,#ec8db3 65%,#b9b6b8)"></div></div>
      <div class="rating"><svg fill="var(--pink)" stroke="var(--heart-line)"><use href="#heart"/></svg><svg fill="var(--pink)" stroke="var(--heart-line)"><use href="#heart"/></svg><svg fill="#fff" stroke="var(--heart-line)"><use href="#heart"/></svg><svg fill="#fff" stroke="var(--heart-line)"><use href="#heart"/></svg><svg fill="#fff" stroke="var(--heart-line)"><use href="#heart"/></svg></div></div>
    <div class="entry" style="left:600px"><div class="thumb"><div class="photo" role="img" aria-label="White round cake topped with pink roses" style="background:linear-gradient(180deg,#fff 10%,#e88aa6 30%,#f6f2ec 55%,#e8b060 80%,#fff)"></div></div>
      <div class="rating"><svg fill="var(--pink)" stroke="var(--heart-line)"><use href="#heart"/></svg><svg fill="var(--pink)" stroke="var(--heart-line)"><use href="#heart"/></svg><svg fill="var(--pink)" stroke="var(--heart-line)"><use href="#heart"/></svg><svg fill="url(#halfFill)" stroke="var(--heart-line)"><use href="#heart"/></svg><svg fill="#fff" stroke="var(--heart-line)"><use href="#heart"/></svg></div></div>
    <div class="entry" style="left:750px"><div class="thumb"><div class="photo" role="img" aria-label="White wedding cake among flowers" style="background:linear-gradient(135deg,#e4e8d0,#f7f4ee 45%,#c9a3c8 80%,#e6d7e0)"></div></div>
      <div class="rating"><svg fill="var(--pink)" stroke="var(--heart-line)"><use href="#heart"/></svg><svg fill="var(--pink)" stroke="var(--heart-line)"><use href="#heart"/></svg><svg fill="var(--pink)" stroke="var(--heart-line)"><use href="#heart"/></svg><svg fill="url(#halfFill)" stroke="var(--heart-line)"><use href="#heart"/></svg><svg fill="#fff" stroke="var(--heart-line)"><use href="#heart"/></svg></div></div>
    <div class="divider"></div>
  </div>

  <div class="row">
    <div class="entry" style="left:0"><div class="thumb"><div class="photo" role="img" aria-label="Chocolate cake with a strawberry" style="background:radial-gradient(ellipse at 50% 55%,#3f2a24 0%,#4e3530 40%,#f4f4f4 65%,#fff)"></div></div>
      <div class="rating"><svg fill="var(--pink)" stroke="var(--heart-line)"><use href="#heart"/></svg><svg fill="url(#halfFill)" stroke="var(--heart-line)"><use href="#heart"/></svg><svg fill="#fff" stroke="var(--heart-line)"><use href="#heart"/></svg><svg fill="#fff" stroke="var(--heart-line)"><use href="#heart"/></svg><svg fill="#fff" stroke="var(--heart-line)"><use href="#heart"/></svg></div></div>
    <div class="entry" style="left:150px"><div class="thumb"><div class="photo" role="img" aria-label="Strawberry cheesecake" style="background:radial-gradient(ellipse at 45% 45%,#d8342e 0%,#e0554a 30%,#f3ead8 55%,#eee)"></div></div>
      <div class="rating"><svg fill="#fff" stroke="var(--heart-line)"><use href="#heart"/></svg><svg fill="#fff" stroke="var(--heart-line)"><use href="#heart"/></svg><svg fill="#fff" stroke="var(--heart-line)"><use href="#heart"/></svg><svg fill="#fff" stroke="var(--heart-line)"><use href="#heart"/></svg><svg fill="#fff" stroke="var(--heart-line)"><use href="#heart"/></svg></div></div>
    <div class="entry" style="left:300px"><div class="thumb"><div class="photo" role="img" aria-label="Chocolate cake with chocolate curls" style="background:radial-gradient(ellipse at 50% 50%,#4a2a1c 0%,#5e3826 40%,#fff 68%)"></div></div>
      <div class="rating"><svg fill="var(--pink)" stroke="var(--heart-line)"><use href="#heart"/></svg><svg fill="var(--pink)" stroke="var(--heart-line)"><use href="#heart"/></svg><svg fill="#fff" stroke="var(--heart-line)"><use href="#heart"/></svg><svg fill="#fff" stroke="var(--heart-line)"><use href="#heart"/></svg><svg fill="#fff" stroke="var(--heart-line)"><use href="#heart"/></svg></div></div>
    <div class="entry" style="left:450px"><div class="thumb"><div class="photo" role="img" aria-label="Small pink first-birthday cake on a stand" style="background:radial-gradient(ellipse at 50% 55%,#f4b6c8 0%,#f8d6e0 20%,#fff 42%)"></div></div>
      <div class="rating"><svg fill="#fff" stroke="var(--heart-line)"><use href="#heart"/></svg><svg fill="#fff" stroke="var(--heart-line)"><use href="#heart"/></svg><svg fill="#fff" stroke="var(--heart-line)"><use href="#heart"/></svg><svg fill="#fff" stroke="var(--heart-line)"><use href="#heart"/></svg><svg fill="#fff" stroke="var(--heart-line)"><use href="#heart"/></svg></div></div>
    <div class="entry" style="left:600px"><div class="thumb"><div class="photo" role="img" aria-label="Striped pink cake on a pink damask backdrop" style="background:linear-gradient(180deg,#e78a9e,#f0c7c0 45%,#d4738a 80%,#e78a9e)"></div></div>
      <div class="rating"><svg fill="var(--pink)" stroke="var(--heart-line)"><use href="#heart"/></svg><svg fill="var(--pink)" stroke="var(--heart-line)"><use href="#heart"/></svg><svg fill="var(--pink)" stroke="var(--heart-line)"><use href="#heart"/></svg><svg fill="url(#halfFill)" stroke="var(--heart-line)"><use href="#heart"/></svg><svg fill="#fff" stroke="var(--heart-line)"><use href="#heart"/></svg></div></div>
    <div class="entry" style="left:750px"><div class="thumb"><div class="photo" role="img" aria-label="Tall white cake on a red and gold backdrop" style="background:linear-gradient(180deg,#c92b1f 0%,#d9382a 50%,#f6efd8 62%,#e8b340 78%,#f0c050)"></div></div>
      <div class="rating"><svg fill="var(--pink)" stroke="var(--heart-line)"><use href="#heart"/></svg><svg fill="var(--pink)" stroke="var(--heart-line)"><use href="#heart"/></svg><svg fill="var(--pink)" stroke="var(--heart-line)"><use href="#heart"/></svg><svg fill="url(#halfFill)" stroke="var(--heart-line)"><use href="#heart"/></svg><svg fill="#fff" stroke="var(--heart-line)"><use href="#heart"/></svg></div></div>
    <div class="divider"></div>
  </div>
</div>

<div class="pager">Page 1 of 3</div>

<ul class="footer-col" style="left:157px">
  <li>Wedding cakes</li><li>Birthday cakes</li><li>Christening cakes</li><li>Creative cakes</li><li>Celebration cakes</li><li>Special event</li>
</ul>
<ul class="footer-col" style="left:308px">
  <li>Home</li><li>Browse</li><li>Tour</li><li>Contact</li><li>Log In</li>
</ul>
<ul class="footer-col" style="left:457px">
  <li>User agreement</li><li>Privacy policy</li><li>Sitemap</li>
</ul>
<div class="social" aria-hidden="true"><span></span><span></span></div>
<div class="copyright">© Copyright 2012<br>Frostwerkly.com</div>

</body>
</html>
```